Facebook Ad for Black Friday 25% off Sitewide

Hi I need a really good FB/Instagram Ad for Black Friday using the pictures of our jackets in our store. Should be size best for FB and Instagram which is 1200 x 628.Our jackets are our #1 selling product in our store. Yellow being #1 best selling and Black is the #2 Best Selling.

Black Friday Sale Promotion-25% off our entire website-Friday Only

Target Market(s)

Girls age 18-35

Industry/Entity Type

Fashion

Requirements
Must have
• Black Background, jackets displayed nicely maybe with some peace signs like my logo or whatever you think would make a good black friday ad.
Nice to have
• Something that really pops
Should not have
• Boring

```html
<!DOCTYPE html>
<html lang="en">
<head>
<meta charset="UTF-8">
<title>Meadow Outpost – Black Friday Sale</title>
<link rel="stylesheet" href="https://fonts.googleapis.com/css2?family=Germania+One&family=Dosis:wght@400;500&family=Tinos:wght@400;700&family=Ubuntu:wght@400&display=swap">
<style>
  :root {
    --frame: #ffffff;
    --night: #050505;
    --facet: #1c1c1e;
    --gold: #e9cf6e;
    --gold-light: #fbeeb0;
    --gold-deep: #b8901f;
    --cream: #f6e7a9;
    --white: #ffffff;
    --jacket-yellow: #f1e12a;
    --jacket-grey: #8d949c;
  }
  * { margin: 0; padding: 0; box-sizing: border-box; }
  html, body { width: 1200px; height: 636px; overflow: hidden; background: var(--frame); }
  .ad {
    position: relative;
    width: 1200px; height: 636px;
    background: var(--frame);
  }
  .stage {
    position: absolute;
    left: 12px; top: 10px; width: 1160px; height: 610px;
    background:
      radial-gradient(ellipse at 62% 38%, var(--facet) 0%, #0d0d0e 45%, var(--night) 80%);
    overflow: hidden;
  }
  .product-photo {
    position: absolute;
    left: 40px; top: 40px; width: 456px; height: 458px;
    border-radius: 30px 30px 10px 10px;
    background:
      linear-gradient(180deg, var(--jacket-grey) 0%, #b7b3ab 26%, var(--jacket-yellow) 34%, #f3e33a 80%, var(--jacket-grey) 86%, #7e858d 100%);
  }
  .brand {
    position: absolute;
    right: 42px; top: 44px;
    display: flex; align-items: center; gap: 14px;
  }
  .brand-dot {
    width: 58px; height: 58px; border-radius: 50%;
    background: var(--gold);
  }
  .brand-name {
    font-family: "Dosis", sans-serif;
    font-weight: 500;
    font-size: 36px;
    line-height: 1;
    color: var(--gold);
  }
  .headline {
    position: absolute;
    left: 518px; right: 42px; top: 178px;
    text-align: right;
    font-family: "Germania One", serif;
    font-weight: 400;
    font-size: 100px;
    line-height: 1.1;
    background: linear-gradient(180deg, var(--gold-light) 0%, var(--gold) 45%, var(--gold-deep) 100%);
    -webkit-background-clip: text; background-clip: text;
    color: transparent;
    white-space: nowrap;
  }
  .subhead {
    position: absolute;
    right: 48px; top: 308px;
    font-family: "Dosis", sans-serif;
    font-weight: 400;
    font-size: 46px;
    line-height: 1;
    color: var(--cream);
  }
  .offer-terms {
    position: absolute;
    right: 234px; top: 388px;
    text-align: right;
    font-family: "Tinos", serif;
    font-weight: 700;
    font-size: 29px;
    line-height: 44px;
    letter-spacing: 1px;
    color: var(--cream);
  }
  .offer-value {
    position: absolute;
    left: 950px; top: 384px;
    font-family: "Tinos", serif;
    color: var(--white);
  }
  .offer-off { display: block; font-size: 32px; line-height: 1; letter-spacing: 1px; margin-left: 6px; }
  .offer-number { font-size: 110px; line-height: 0.9; }
  .offer-percent { font-size: 46px; }
  .site-url {
    position: absolute;
    right: 54px; top: 548px;
    font-family: "Ubuntu", sans-serif;
    font-size: 30px;
    letter-spacing: 3.8px;
    color: var(--cream);
  }
  .icon-row {
    position: absolute;
    left: 164px; top: 532px;
    display: flex; align-items: center; gap: 22px;
  }
  .icon-art {
    width: 42px; height: 46px; border-radius: 6px;
    background: linear-gradient(180deg, var(--gold-light), var(--gold-deep));
  }
  .icon-art.small { width: 26px; height: 40px; }
  .icon-row svg { display: block; }
</style>
</head>
<body>
<main class="ad">
  <section class="stage">
    <div class="product-photo" role="img" aria-label="Yellow quilted puffer jacket with grey knit hood, faux-fur collar and knit hem"></div>

    <div class="brand">
      <span class="brand-dot"></span>
      <span class="brand-name">Meadow Outpost</span>
    </div>

    <h1 class="headline">Black Friday</h1>
    <p class="subhead">Sale Promotion</p>

    <p class="offer-terms">OUR ENTIRE<br>WEBSITE<br>FRIDAY ONLY</p>
    <p class="offer-value">
      <span class="offer-off">OFF</span>
      <span class="offer-number">25</span><span class="offer-percent">%</span>
    </p>

    <p class="site-url">www.meadowoutpost.com</p>

    <div class="icon-row">
      <div class="icon-art" role="img" aria-label="Gold meditating figure icon"></div>
      <svg class="icon-heart" width="34" height="30" viewBox="0 0 34 30" aria-hidden="true">
        <path d="M17 29 C6 20 1 14 1 8.5 A7.5 7.5 0 0 1 17 6 A7.5 7.5 0 0 1 33 8.5 C33 14 28 20 17 29 Z" fill="var(--gold)"/>
      </svg>
      <svg class="icon-peace" width="32" height="32" viewBox="0 0 32 32" aria-hidden="true">
        <circle cx="16" cy="16" r="14" fill="none" stroke="var(--gold)" stroke-width="3"/>
        <path d="M16 2 V30 M16 16 L6 26 M16 16 L26 26" stroke="var(--gold)" stroke-width="3" fill="none"/>
      </svg>
      <div class="icon-art small" role="img" aria-label="Gold victory hand sign icon"></div>
    </div>
  </section>
</main>
</body>
</html>
```